Luxury Face Oil Label

I'm looking for a simple and sophisticated design for a natural face oil that will target the luxe market. It is a pure Natural product. I have attached the logo, Velumi Organics.

Here's the Copy

LUXE FACIAL OIL

Regenerate. Hydrate. Glow

100% Natural

30ml (1.01 oz)

A complex blend of Pure Oils including Marula, Sea Buckthorn, Rosehip, Neroli, Evening primrose, Argan, Calendula, Lavender, Jojoba, Grapeseed, Baobab, Moringa and Vitamin E oil.

Produced by
Brasso Kettle Ltd
P.O box 7925-00300
Nairobi, Kenya
www.velumiorganics.example

Target Market(s)

High end

Requirements
Must have
• Simple, Please consider the bottle, which is a 30ml clear glass bottle with a gold and white pump. Image attached.
Nice to have
• Very clean designs, not too much going on.
Should not have
• Leaves and nuts.

```html
<!DOCTYPE html>
<html lang="en">
<head>
<meta charset="utf-8">
<title>Velumi Organics – Luxe Facial Oil Label</title>
<link rel="stylesheet" href="https://fonts.googleapis.com/css2?family=Cormorant+Garamond:wght@400;500&family=Mulish:wght@400;700&display=swap">
<style>
  :root {
    --backdrop: #878273;
    --label-light: #f7f7f8;
    --label-shade: #e4e5e8;
    --band: #5b5e52;
    --band-text: #cfd0c9;
    --tag: #b5b59b;
    --tag-text: #45473c;
    --ink: #5a5a58;
    --ink-soft: #8a8a88;
    --ink-strong: #4e4f4b;
    --natural-green: #4fae5a;
    --frame: #d9d5cc;
    --art: #d8d9d6;
  }
  * { box-sizing: border-box; margin: 0; padding: 0; }
  html, body { width: 1151px; height: 1200px; overflow: hidden; }
  body { background: var(--backdrop); position: relative; font-family: "Mulish", sans-serif; }

  .label {
    position: absolute; left: 30px; top: 381px;
    width: 1386px; height: 555px;
    transform: scale(0.7872); transform-origin: top left;
    background: linear-gradient(100deg, var(--label-light) 0%, var(--label-shade) 30%, var(--label-light) 45%, var(--label-shade) 70%, var(--label-light) 100%);
    overflow: hidden;
  }
  .edge-strip { position: absolute; left: 0; top: 0; width: 31px; height: 100%; background: var(--band); }
  .edge-strip--right { left: auto; right: 0; width: 7px; }

  .blend-tag {
    position: absolute; left: 0; top: 222px; width: 172px; height: 113px;
    background: var(--tag); border-radius: 0 22px 22px 0;
    padding: 15px 0 0 26px;
    font-size: 20px; line-height: 21px; color: var(--tag-text); letter-spacing: -0.5px;
    text-transform: uppercase;
  }
  .ingredients { position: absolute; left: 190px; top: 30px; list-style: none; }
  .ingredients li {
    height: 39.2px; display: flex; align-items: center;
    font-size: 21px; color: var(--ink); letter-spacing: 0.3px;
  }
  .ingredients li::before {
    content: ""; width: 28px; height: 2px; background: var(--ink-soft); margin-right: 18px;
  }

  .brand {
    position: absolute; width: 140px; height: 140px;
    display: flex; flex-direction: column; align-items: center; justify-content: center;
    font-family: "Cormorant Garamond", serif; font-weight: 500;
    color: var(--ink); letter-spacing: 4px; text-transform: uppercase; font-size: 18px; line-height: 24px;
    text-align: center;
  }
  .brand--front { left: 501px; top: 60px; }
  .brand--back { left: 996px; top: 140px; width: 160px; height: 156px; font-size: 20px; line-height: 27px; }

  .branch-art { position: absolute; left: 700px; top: 35px; width: 115px; height: 480px;
    background: linear-gradient(180deg, transparent 0%, var(--art) 15%, var(--art) 85%, transparent 100%); opacity: .6; border-radius: 40px 0 0 40px; }

  .luxe-band { position: absolute; left: 815px; top: 0; width: 109px; height: 100%; background: var(--band);
    display: flex; align-items: center; justify-content: center; }
  .luxe-band span {
    writing-mode: vertical-rl; transform: rotate(180deg);
    font-family: "Cormorant Garamond", serif; font-weight: 500; font-size: 88px;
    letter-spacing: 38px; color: var(--band-text); margin-top: 20px;
  }

  .product-name { position: absolute; left: 497px; top: 385px;
    font-family: "Cormorant Garamond", serif; font-weight: 500; font-size: 38px; letter-spacing: 1px; color: var(--ink); }
  .benefits { position: absolute; left: 497px; top: 425px;
    font-family: "Cormorant Garamond", serif; font-size: 18px; letter-spacing: 0.5px; color: var(--ink-soft); }

  .natural-mark { position: absolute; left: 497px; top: 482px; width: 123px; height: 55px;
    border: 3px solid var(--natural-green); border-radius: 8px;
    display: flex; flex-direction: column; align-items: center; justify-content: center;
    font-weight: 700; color: var(--natural-green); font-size: 20px; line-height: 19px; text-transform: uppercase; }

  .volume { position: absolute; left: 710px; top: 478px; text-align: center;
    font-family: "Cormorant Garamond", serif; color: var(--ink-strong); font-size: 26px; line-height: 26px; }
  .volume small { display: block; font-size: 12px; line-height: 12px; color: var(--ink-soft); }

  .producer { position: absolute; left: 994px; top: 394px; font-size: 20px; line-height: 25.5px; color: var(--ink); }
  .producer strong { font-weight: 700; color: var(--ink-strong); }
</style>
</head>
<body>
  <section class="label" aria-label="Luxe facial oil bottle label">
    <div class="edge-strip"></div>

    <div class="blend-tag">A complex<br>blend of<br>pure oils<br>including</div>
    <ul class="ingredients">
      <li>Marula,</li><li>Sea Buckthorn,</li><li>Rosehip,</li><li>Neroli,</li>
      <li>Evening primrose,</li><li>Argan,</li><li>Calendula,</li><li>Lavender,</li>
      <li>Jojoba,</li><li>Grapeseed,</li><li>Baobab,</li><li>Moringa</li><li>Vitamin E oil.</li>
    </ul>

    <div class="brand brand--front">Velumi<br>Organics</div>
    <div class="branch-art" role="img" aria-label="Fine line botanical branch illustration"></div>
    <h1 class="product-name">FACIAL OIL</h1>
    <p class="benefits">REGENERATE | HYDRATE | GLOW</p>
    <div class="natural-mark"><span>100%</span><span>Natural</span></div>
    <p class="volume">30ML<small>(1.01 oz)</small></p>

    <div class="luxe-band"><span>LUXE</span></div>

    <div class="brand brand--back">Velumi<br>Organics</div>
    <address class="producer" style="font-style:normal">
      Produced by<br>
      <strong>Brasso Kettle Ltd</strong><br>
      P.O box 7925-00300<br>
      Nairobi, Kenya<br>
      <strong>www.velumiorganics.example</strong>
    </address>

    <div class="edge-strip edge-strip--right"></div>
  </section>
</body>
</html>
```